Brisk Hollow Builders Needs A Flyer

We need a flyer for our newest product "The Cedarlane Garden Workroom"

Here is some copy for the flyer:

1. More and more people everyday are working from home and finding it difficult to disconnect from home activities in order to focus on their work. They are also finding it very expensive to add on to their existing house for a quiet place. Our archatectually stunning, Cedarlane Garden Workroom is the answer. The office studio measures 16' wide and 10' deep. 160 Square feet of space.

Perfect for dozens of purposes. Home office, design studio, artist studio, home school office, reading room, craft studio, drafting room.

Features include:

- Steel Framing. 40-60% lighter then wood, higher strength to weight ratio, resistant to mold and fire and steel is the most recycled material on earth!
- Spray foam insulation. Cool in the summer and warm in the winter.
- HVAC Mini Split with wireless remote control and thermostat.
- 100% Off grid with enough solar and battery storage to run your entire office. No need to pay for an expensive electric installation.
- Flush fitting floor outlets to reduce wires.
- TV mount (Optional with pre-wired electric, HDMI, digital audio & Cat 6)
- Windows are tempered glass custom made by Morvik Glazing.
- Solar qualifies for a 26% tax credit. This is not a write-off rather it is a direct reduction on your tax obligation.
- Thousands of dollars less than adding onto your home.
- Custom color, siding, features available.

This beautiful back yard office is delivered 100% assembled and ready to enjoy on the day of delivery.

We ship nationwide from our factory in South Carolina. Give us a call anytime to speak to a designer and start your dream office today!

555-318-4027
info@BriskHollowBuilders.example

```html
<!DOCTYPE html>
<html lang="en">
<head>
<meta charset="utf-8">
<title>The Cedarlane Garden Workroom – Brisk Hollow Builders</title>
<link rel="stylesheet" href="https://fonts.googleapis.com/css2?family=Oswald:wght@500;700&family=Roboto:wght@400;700;900&display=swap">
<style>
  :root {
    --green: #5fa346;
    --green-dark: #3f7f2e;
    --gold: #e3a21f;
    --gold-dark: #b97d12;
    --ink: #111111;
    --paper: #ffffff;
    --page-bg: #2a2a2a;
  }
  * { box-sizing: border-box; margin: 0; padding: 0; }
  html, body { width: 1015px; height: 1200px; overflow: hidden; background: var(--page-bg); }
  .flyer {
    position: relative; width: 1015px; height: 1200px; overflow: hidden;
    background: var(--paper); font-family: "Roboto", Arial, sans-serif; color: var(--ink);
  }
  .abs { position: absolute; }
  .photo-front {
    left: 0; top: 0; width: 640px; height: 300px;
    background: linear-gradient(180deg, #c9d8c0 0%, #7c9667 45%, #3f4a3c 70%, #8b9a7a 100%);
  }
  .photo-side {
    left: 440px; top: 270px; width: 575px; height: 310px;
    background: linear-gradient(180deg, #a9c39a 0%, #5c7a4c 30%, #4a4d4f 55%, #3a3c3e 80%, #6f8a5c 100%);
  }
  .brand-box {
    left: 640px; top: 0; width: 375px; height: 270px; background: var(--paper);
    display: flex; align-items: center; justify-content: center; gap: 12px;
  }
  .brand-mark { width: 22px; height: 22px; border-radius: 50%; background: var(--green); }
  .brand-name {
    font-family: "Oswald", sans-serif; font-weight: 700; font-size: 34px;
    color: var(--green-dark); text-transform: uppercase; line-height: 1.05; letter-spacing: 0.5px;
  }
  .shapes { left: 0; top: 0; width: 1015px; height: 1200px; }
  .headline {
    left: 55px; top: 318px; width: 395px;
    font-family: "Oswald", sans-serif; font-weight: 700; font-size: 56px; line-height: 1.05;
    color: var(--paper); text-transform: uppercase; white-space: nowrap;
  }
  .headline span { display: block; }
  .framing-art {
    left: 40px; top: 600px; width: 220px; height: 80px;
    background: linear-gradient(180deg, #c98c18, #a86f0e);
  }
  .purposes { left: 280px; top: 532px; width: 720px; text-align: center; text-transform: uppercase; }
  .purposes-title { font-family: "Roboto", sans-serif; font-weight: 900; font-size: 24px; line-height: 1.1; }
  .purposes-list { font-size: 18px; line-height: 1.2; margin-top: 6px; }
  .intro {
    left: 55px; top: 715px; width: 345px; text-transform: uppercase;
    font-size: 15.5px; line-height: 1.32; color: var(--green);
  }
  .intro strong { font-weight: 900; }
  .features { left: 420px; top: 705px; width: 575px; }
  .features-tag {
    display: inline-block; background: var(--green); color: var(--paper);
    font-weight: 700; font-size: 19px; padding: 3px 28px 3px 10px;
    clip-path: polygon(0 0, 100% 0, 88% 100%, 0 100%);
    text-transform: uppercase;
  }
  .feature-list { list-style: none; margin-top: 8px; }
  .feature-list li {
    position: relative; padding-left: 22px; font-size: 13.2px; line-height: 1.32; margin-bottom: 2px;
  }
  .feature-list li::before {
    content: ""; position: absolute; left: 4px; top: 6px; width: 7px; height: 7px;
    border-radius: 50%; background: var(--green);
  }
  .delivery-bar {
    left: 60px; top: 1020px; width: 895px; height: 58px; border-radius: 16px;
    background: var(--green); color: var(--paper); text-align: center; text-transform: uppercase;
    font-weight: 700; font-size: 17.5px; line-height: 1.25; padding-top: 5px;
  }
  .ship-note {
    left: 55px; top: 1090px; width: 640px; text-transform: uppercase;
    font-weight: 900; font-size: 14.5px; line-height: 1.25;
  }
  .phone {
    left: 720px; top: 1094px; display: flex; align-items: center; gap: 10px;
    font-family: "Oswald", sans-serif; font-weight: 500; font-size: 28px; color: var(--gold);
  }
  .footer {
    left: 0; top: 1140px; width: 1015px; height: 60px; background: var(--ink);
    display: flex; align-items: center; gap: 14px; padding-left: 60px;
    font-family: "Oswald", sans-serif; font-weight: 500; font-size: 26px; color: var(--gold);
    text-transform: uppercase;
  }
  .icon-circle {
    width: 32px; height: 32px; border-radius: 50%; background: var(--paper);
    display: flex; align-items: center; justify-content: center;
  }
  .icon-circle.outlined { border: 2px solid var(--ink); }
</style>
</head>
<body>
<div class="flyer">
  <div class="abs photo-front" role="img" aria-label="Photo of the garden workroom front with glass doors in a landscaped yard"></div>
  <div class="abs photo-side" role="img" aria-label="Photo of the workroom side wall with solar panels on the roof"></div>

  <div class="abs brand-box">
    <span class="brand-mark"></span>
    <span class="brand-name">Brisk Hollow<br>Builders</span>
  </div>

  <svg class="abs shapes" viewBox="0 0 1015 1200" aria-hidden="true">
    <polygon points="0,295 445,295 445,300 460,560 0,598" fill="#5fa346"/>
    <polyline points="0,571 640,484 1015,552" fill="none" stroke="#ffffff" stroke-width="6"/>
    <polygon points="0,576 640,490 1015,557 1015,690 0,690" fill="#e3a21f"/>
  </svg>

  <h1 class="abs headline"><span>The Cedarlane</span><span>Garden</span><span>Workroom</span></h1>

  <div class="abs framing-art" role="img" aria-label="Illustration of the steel frame structure"></div>

  <div class="abs purposes">
    <p class="purposes-title">Perfect for<br>dozens of purposes</p>
    <p class="purposes-list">Home office, design studio, artist studio,<br>home school office, reading room,<br>craft studio, drafting room.</p>
  </div>

  <p class="abs intro">More and more people everyday are working from home and finding it difficult to disconnect from home activities in order to focus on their work. They are also finding it very expensive to add on to their existing house for a quiet place. <strong>Our archatectually stunning, Cedarlane Garden Workroom is the answer. The office studio measures 16' wide and 10' deep. 160 square feet of space.</strong></p>

  <div class="abs features">
    <span class="features-tag">Features</span>
    <ul class="feature-list">
      <li>Steel Framing. 40-60% lighter then wood, higher strength to weight ratio, resistant to mold and fire and steel is the most recycled material on earth!</li>
      <li>Spray foam insulation. Cool in the summer and warm in the winter.</li>
      <li>HVAC Mini Split with wireless remote control and thermostat.</li>
      <li>100% Off grid with enough solar and battery storage to run your entire office. No need to pay for an expensive electric installation.</li>
      <li>Flush fitting floor outlets to reduce wires.</li>
      <li>TV mount (Optional with pre-wired electric, HDMI, digital audio &amp; Cat 6)</li>
      <li>Windows are tempered glass custom made by Morvik Glazing.</li>
      <li>Solar qualifies for a 26% tax credit. This is not a write-off rather it is a direct reduction on your tax obligation.</li>
      <li>Thousands of dollars less than adding onto your home.</li>
      <li>Custom color, siding, features available.</li>
    </ul>
  </div>

  <div class="abs delivery-bar">This beautiful back yard office is delivered 100%<br>assembled and ready to enjoy on the day of delivery.</div>

  <p class="abs ship-note">We ship nationwide from our factory in South Carolina. Give us a call anytime to speak to a designer and start your dream office today!</p>

  <div class="abs phone">
    <span class="icon-circle outlined">
      <svg width="18" height="18" viewBox="0 0 24 24" aria-hidden="true"><path d="M6.6 10.8a15.1 15.1 0 0 0 6.6 6.6l2.2-2.2c.3-.3.7-.4 1-.2 1.1.4 2.300.6 3.6.6.6 0 1 .4 1 1V20c0 .6-.4 1-1 1C10.6 21 3 13.4 3 4c0-.6.4-1 1-1h3.5c.6 0 1 .4 1 1 0 1.3.2 2.5.6 3.6.1.3 0 .7-.2 1z" fill="#111"/></svg>
    </span>
    555-318-4027
  </div>

  <div class="abs footer">
    <span class="icon-circle">
      <svg width="18" height="14" viewBox="0 0 24 18" aria-hidden="true"><rect x="1" y="1" width="22" height="16" fill="none" stroke="#111" stroke-width="2"/><polyline points="1,1 12,10 23,1" fill="none" stroke="#111" stroke-width="2"/></svg>
    </span>
    info@BriskHollowBuilders.example
  </div>
</div>
</body>
</html>
```